Ridge Gathering presented by The Lantern

This is a one-day seminar for men who want to grow mentally, spiritually and financially.
Host Pastor Gordon Whitlock
Special guest: Dr. Frank Dunmore, Dr. Brenda Soward

Target Market(s)

Men 18-55

Colors

Designer to choose colors to be used in the design.

Requirements
Must have
• clean designs
Nice to have
• A clean design that translates to social media and websites

```html
<!DOCTYPE html>
<html lang="en">
<head>
<meta charset="utf-8">
<title>Ridge Gathering – Seminar Flyer</title>
<link rel="stylesheet" href="https://fonts.googleapis.com/css2?family=Montserrat:wght@300;400;600;700;800;900&display=swap">
<style>
  :root {
    --red-light: #d92a38;
    --red-deep: #bf1f2e;
    --white: #ffffff;
    --ink-shadow: rgba(60, 8, 14, 0.55);
    --page: #ffffff;
    --photo-light: #f2f0ef;
    --photo-mid: #cfc9c7;
  }
  * { margin: 0; padding: 0; box-sizing: border-box; }
  html, body { width: 1200px; height: 1200px; overflow: hidden; background: var(--page); }
  body { position: relative; font-family: "Montserrat", sans-serif; color: var(--white); }

  .flyer {
    position: absolute; left: 186px; top: 20px; width: 827px; height: 1160px;
    background: radial-gradient(ellipse at 50% 40%, var(--red-light) 0%, var(--red-deep) 100%);
    overflow: hidden;
  }
  .frame-line { position: absolute; background: var(--white); }
  .frame-top-left   { left: 24px;  top: 85px; width: 272px; height: 2px; }
  .frame-top-right  { left: 535px; top: 85px; width: 269px; height: 2px; }
  .frame-left   { left: 24px;  top: 85px; width: 2px; height: 1050px; }
  .frame-right  { left: 802px; top: 85px; width: 2px; height: 1050px; }
  .frame-bottom { left: 24px;  top: 1133px; width: 780px; height: 2px; }

  .centered { position: absolute; left: 0; width: 100%; text-align: center; }

  .presenter-name { top: 62px; font-size: 30px; font-weight: 700; letter-spacing: 1px; }
  .presents { top: 148px; font-size: 18px; font-weight: 400; }

  .event-title {
    top: 183px; font-size: 70px; font-weight: 900; letter-spacing: -1px; line-height: 1;
    text-shadow: 3px 4px 0 var(--ink-shadow), 0 0 12px rgba(255,255,255,0.35);
  }
  .tagline-light { top: 286px; font-size: 24px; font-weight: 300; }
  .tagline-bold  { top: 317px; font-size: 25px; font-weight: 700; letter-spacing: -0.3px; }

  .host-label { top: 366px; font-size: 22px; font-weight: 300; }
  .host-name {
    top: 393px; font-size: 38px; font-weight: 900; letter-spacing: -0.5px;
    text-shadow: 2px 3px 0 var(--ink-shadow);
  }

  .portrait {
    position: absolute; border-radius: 50%;
    border: 10px solid var(--white);
    background: radial-gradient(circle at 50% 45%, var(--photo-light) 0%, var(--photo-mid) 100%);
    box-shadow: 0 0 0 3px rgba(255,255,255,0.35);
  }
  .portrait-host  { left: 280px; top: 464px; width: 268px; height: 268px; }
  .portrait-guest-left  { left: 98px;  top: 826px; width: 224px; height: 224px; }
  .portrait-guest-right { left: 504px; top: 826px; width: 224px; height: 224px; }

  .guest-heading { top: 770px; font-size: 22px; font-weight: 800; }
  .guest-heading::before, .guest-heading::after {
    content: ""; display: inline-block; width: 62px; height: 2px; background: var(--white);
    vertical-align: middle; margin: 0 8px;
  }

  .guest-name { position: absolute; top: 1074px; width: 260px; text-align: center; font-size: 17px; font-weight: 800; }
  .guest-name-left  { left: 80px; }
  .guest-name-right { left: 486px; }

  .website { top: 1104px; font-size: 19px; font-weight: 400; letter-spacing: 4px; }
</style>
</head>
<body>
  <main class="flyer">
    <div class="frame-line frame-top-left"></div>
    <div class="frame-line frame-top-right"></div>
    <div class="frame-line frame-left"></div>
    <div class="frame-line frame-right"></div>
    <div class="frame-line frame-bottom"></div>

    <p class="centered presenter-name">The Lantern</p>
    <p class="centered presents">PRESENTS</p>

    <h1 class="centered event-title">RIDGE GATHERING</h1>
    <p class="centered tagline-light">WANT TO GROW</p>
    <p class="centered tagline-bold">MENTALLY, SPIRITUALLY &amp; FINANCIALLY</p>

    <p class="centered host-label">HOST PASTOR</p>
    <h2 class="centered host-name">GORDON WHITLOCK</h2>

    <div class="portrait portrait-host" role="img" aria-label="Portrait photo of host pastor Gordon Whitlock in a white shirt"></div>

    <p class="centered guest-heading">SPECIAL GUEST</p>

    <div class="portrait portrait-guest-left" role="img" aria-label="Portrait photo of Dr. Brenda Soward"></div>
    <div class="portrait portrait-guest-right" role="img" aria-label="Portrait photo of Dr. Frank Dunmore"></div>

    <p class="guest-name guest-name-left">DR. BRENDA SOWARD</p>
    <p class="guest-name guest-name-right">DR. FRANK DUNMORE</p>

    <p class="centered website">WWW.RIDGEGATHERING-EVENTS.COM</p>
  </main>
</body>
</html>
```